Infant Massage Instructor Business Card Design

I need a business card in order to advertise my private and group parent instruction classes for massaging their infants. I am in Boulder, Colorado. I most often teach people in their own homes, but will offer group classes in other public facility venues.
I would like to use peach and lavender/ purple colors, very soft, round but clearly legible font and design. I would love to have a simple, sweeping, soft line graphic of an infant (perhaps held in adult hands?) reaching towards my business name; "Tenderly Tended Infant Massage". "Power Points" are: Reading Infant Cues, Strengthening Parent Intuition, and Nurturing Family Bonds.
"Private and group classes offered, sliding scale rates available."
THE ATTACHED LOGO IS THE LOGO OF THE "GLOBAL SOCIETY FOR BABY TOUCH", my R.B.T.P. certifying agency.

"Properly" spelled, my first name has an accent exactly over the 'e'. The top of the accent leans to the right. I would like for the name of the business to appear foremost, over my own name (which is hard for people to pronounce and 'get'). Thank you for your care and creativity in helping me promote this beautiful service offering!

I will be considering a letterhead design and postcard / brochure design as well. Please keep that in mind as you design! Thank you!

Target Market(s)

New moms and dads. Young adults to 50. Single parents, adoptive parents. Mixed economic status.

Industry/Entity Type

Adult

Contact Information for Business Card

Tenderly Tended Infant Massage
Morvel Oskin, R.B.T.P.
303-555-0182

Colors
b868aa
e667a6
a64599
f68e4e
f9bb93
f37123

Requirements
Must have
• Soft, curvy, simple line drawing of infant.
Nice to have
• Infant image, being held in adult hands
Should not have
• No "cutesy" look, please! No cartoon-like images.

```html
<!DOCTYPE html>
<html lang="en">
<head>
<meta charset="utf-8">
<title>Tenderly Tended Infant Massage – Business Card</title>
<link rel="stylesheet" href="https://fonts.googleapis.com/css2?family=Arimo:wght@400;700&display=swap">
<style>
  :root {
    --backdrop: #efe7e2;
    --magenta: #e448e0;
    --deep-purple: #4a1848;
    --orange: #f37123;
    --orange-soft: #f68e4e;
    --peach: #f9bb93;
    --peach-frame: #f4a584;
    --blush: #fde8e2;
    --lavender: #b868aa;
    --purple: #a64599;
    --ink: #2a1f22;
    --tagline: #f7c3a3;
  }
  * { margin: 0; padding: 0; box-sizing: border-box; }
  html, body { width: 1200px; height: 720px; overflow: hidden; }
  body {
    background: var(--backdrop);
    font-family: "Arimo", Arial, sans-serif;
    position: relative;
  }

  .card { position: absolute; box-shadow: 0 6px 18px rgba(60, 30, 20, 0.25); overflow: hidden; }

  /* Front */
  .card-front { left: 57px; top: 178px; width: 504px; height: 294px; background: var(--blush); }
  .front-photo {
    position: absolute; inset: 0;
    background:
      radial-gradient(ellipse at 52% 38%, #f6c9b8 0%, #eeb3a4 38%, #e9c4c0 62%, #f8e6e3 100%);
  }
  .front-headline {
    position: absolute; left: 14px; top: 12px;
    font-weight: 700; font-size: 44px; line-height: 45px; letter-spacing: -2px;
    color: var(--magenta);
    text-shadow: 3px 3px 0 var(--deep-purple);
  }
  .front-mark {
    position: absolute; left: 380px; top: 16px; width: 82px;
    display: flex; flex-direction: column; align-items: center; gap: 8px;
  }
  .mark-circle { width: 80px; height: 80px; border-radius: 50%; background: #f7f1ee; border: 3px solid #4a3a3a; }
  .mark-name { font-weight: 700; font-size: 18px; color: var(--orange); }
  .front-points {
    position: absolute; right: 10px; bottom: 16px; text-align: right;
    font-weight: 700; font-size: 20px; line-height: 24px; letter-spacing: -1px;
    color: var(--tagline);
    text-shadow: 1px 1px 0 #5a3a30, -1px 0 0 #5a3a30;
  }

  /* Back */
  .card-back { left: 623px; top: 262px; width: 502px; height: 295px; background: var(--peach-frame); }
  .back-photo {
    position: absolute; left: 9px; top: 8px; width: 202px; height: 278px;
    background: linear-gradient(160deg, #b9b2ac 0%, #9a948f 45%, #5e5a5b 100%);
  }
  .photo-mark {
    position: absolute; left: 9px; bottom: 8px; width: 56px; height: 56px;
    border-radius: 50%; background: #f7f1ee; border: 3px solid #4a3a3a;
  }
  .back-panel {
    position: absolute; left: 219px; top: 8px; width: 274px; height: 278px;
    background: var(--blush); padding: 8px 6px 0 8px;
  }
  .name-row { display: flex; align-items: baseline; gap: 6px; white-space: nowrap; }
  .name-cred { font-weight: 700; font-size: 13px; color: var(--orange); }
  .name { font-weight: 700; font-size: 30px; letter-spacing: -1px; color: var(--magenta); text-shadow: 2px 2px 0 var(--deep-purple); }
  .title { font-weight: 700; font-size: 11.5px; color: var(--orange); margin-top: 1px; white-space: nowrap; letter-spacing: -0.3px; }
  .business {
    margin-top: 6px; font-weight: 700; font-size: 29px; line-height: 33px; letter-spacing: -1.4px;
    color: var(--magenta); text-shadow: 2px 2px 0 var(--deep-purple); white-space: nowrap;
  }
  .phone {
    margin-top: 6px; font-weight: 700; font-size: 32px; letter-spacing: 0;
    color: var(--orange-soft); text-shadow: 2px 2px 0 var(--ink);
  }
  .services { list-style: none; margin-top: 8px; padding-left: 8px; }
  .services li {
    display: flex; align-items: center; gap: 8px;
    font-weight: 700; font-size: 13px; line-height: 17px; color: var(--ink);
  }
  .services li::before { content: ""; width: 14px; height: 14px; background: var(--bullet); flex: none; }
  .b1 { --bullet: var(--lavender); }
  .b2 { --bullet: var(--purple); }
  .b3 { --bullet: var(--peach); }
  .b4 { --bullet: var(--orange-soft); }
  .b5 { --bullet: var(--orange); }
</style>
</head>
<body>
  <section class="card card-front">
    <div class="front-photo" role="img" aria-label="Photograph of a sleeping newborn baby in soft pink light"></div>
    <h1 class="front-headline">Tenderly<br>Tended<br>Infant<br>Massage</h1>
    <div class="front-mark">
      <div class="mark-circle"></div>
      <span class="mark-name">R.B.T.P.</span>
    </div>
    <p class="front-points">Reading Infant Cues<br>Strengthening Parent Intuition<br>Nurturing Family Bonds.</p>
  </section>

  <section class="card card-back">
    <div class="back-photo" role="img" aria-label="Portrait photograph of the instructor"></div>
    <div class="photo-mark"></div>
    <div class="back-panel">
      <div class="name-row"><span class="name-cred">R.B.T.P.</span><span class="name">Morvel Oskin</span></div>
      <p class="title">Registered Baby Touch Practitioner</p>
      <h2 class="business">Tenderly Tended<br>Infant Massage</h2>
      <p class="phone">303-555-0182</p>
      <ul class="services">
        <li class="b1">Reading Infant Cues</li>
        <li class="b2">Strengthening Parent Intuition</li>
        <li class="b3">Nurturing Family Bonds</li>
        <li class="b4">Private and group classes offered</li>
        <li class="b5">Sliding scale rates available</li>
      </ul>
    </div>
  </section>
</body>
</html>
```